CLU大学院「スキル羅針盤」のバナー作成 を作成していただける方を募集しております。 ■目的・概要 MBA取得検討者向け、ターゲティング広告用に、 コスモリンク大学大学院がプロデュースした「スキル羅針盤」の 新しいバナーの作成依頼です。 ■デザインイメージ 既存のバナーをご参考までに貼付いたします。 このバナーと同等かもしくはそれを上回るクオリティでの作成ができればと思います。 ランディング先のページは下記です。 サイト名:スキル羅針盤 URL: http://www.cosmolink-u.example/sk_lp/ スキル羅針盤は2万人を超える方々が実施しているコンテンツですので、 「診断者数2万人」などの要素をバナー内に入れていただいても結構です。 基本的には製作者様のセンスにお任せしたいと思います。 ■サイズ: 300×250 1枚 ■値段: 5000円 ■納品形式: PSDデータとJPGデータ ■継続について 今回コンペで採用された方には、引き続き他の10個以上のバナーの作成をお願いすることになるので、 ぜひふるってご応募くださいませ! 素敵なバナーになるよう、ぜひお力を貸してください。 たくさんのご応募お待ち致しております! |

```html
<!DOCTYPE html>
<html lang="ja">
<head>
<meta charset="utf-8">
<title>スキル羅針盤 バナー</title>
<link rel="stylesheet" href="https://fonts.googleapis.com/css2?family=Noto+Sans+JP:wght@500;700;900&family=Roboto:wght@500;700&display=swap">
<style>
  :root {
    --page: #ffffff;
    --night: #1a0b07;
    --ember: #4a2317;
    --rust: #6b3323;
    --gold-light: #fff3c4;
    --gold: #e0b44c;
    --gold-deep: #8a5a12;
    --red: #c8101a;
    --red-deep: #8e0710;
    --white: #ffffff;
    --ink: #1b1b1b;
    --frame: #2a2a2a;
  }
  * { margin: 0; padding: 0; box-sizing: border-box; }
  html, body {
    width: 1200px; height: 1007px; overflow: hidden;
    background: var(--page);
    font-family: "Noto Sans JP", sans-serif;
  }
  .banner {
    position: absolute; left: 92px; top: 84px;
    width: 1023px; height: 800px;
    background: var(--night);
    border: 3px solid var(--frame);
    overflow: hidden;
  }
  .banner p, .banner h1, .banner div, .banner a { white-space: nowrap; }
  .banner__scene {
    position: absolute; left: 0; top: 0; width: 100%; height: 672px;
    background: radial-gradient(ellipse at 55% 35%, var(--rust) 0%, var(--ember) 45%, var(--night) 100%);
  }
  .ribbon {
    position: absolute; left: 540px; top: 14px;
    width: 430px; height: 84px;
    transform: rotate(-5deg);
    background: linear-gradient(180deg, var(--gold-light) 0%, var(--gold) 55%, var(--gold-deep) 100%);
    clip-path: polygon(0 10%, 100% 0, 96% 50%, 100% 100%, 2% 100%, 5% 55%);
    display: flex; align-items: center; justify-content: center;
    color: var(--red); font-weight: 900; font-size: 42px; line-height: 1;
  }
  .ribbon .num { font-size: 54px; }
  .lead-band {
    position: absolute; left: 330px; top: 112px;
    width: 660px; height: 62px;
    background: linear-gradient(180deg, var(--red) 0%, var(--red-deep) 100%);
    clip-path: polygon(4% 0, 100% 0, 96% 100%, 0 100%);
    color: var(--white); font-weight: 900; font-size: 34px; line-height: 1;
    display: flex; align-items: center; justify-content: center;
  }
  .hook {
    position: absolute; left: 0; top: 202px; width: 100%;
    text-align: center; color: var(--white);
    font-weight: 900; font-size: 40px; line-height: 1.2; letter-spacing: -1px;
    text-shadow: 0 3px 6px rgba(0,0,0,.8);
  }
  .title {
    position: absolute; left: 0; top: 272px; width: 100%;
    text-align: center; font-weight: 900; font-size: 138px; line-height: 1.1;
    letter-spacing: 2px;
    background: linear-gradient(180deg, var(--gold-light) 0%, var(--gold) 45%, var(--gold-deep) 62%, var(--gold) 80%, var(--gold-light) 100%);
    -webkit-background-clip: text; background-clip: text; color: transparent;
    filter: drop-shadow(0 4px 3px rgba(0,0,0,.85));
  }
  .tagline {
    position: absolute; left: 0; top: 486px; width: 100%;
    text-align: center; color: var(--white);
    font-family: "Roboto", sans-serif; font-weight: 500; font-size: 34px; line-height: 1.2;
  }
  .cta {
    position: absolute; left: 28px; top: 572px;
    width: 352px; height: 60px;
    background: linear-gradient(180deg, var(--gold-light) 0%, var(--gold) 50%, var(--gold-deep) 100%);
    border-radius: 6px;
    color: var(--white); font-weight: 900; font-size: 34px; line-height: 1;
    display: flex; align-items: center; justify-content: center; gap: 14px;
    text-shadow: 0 2px 3px rgba(0,0,0,.6);
  }
  .cta svg { width: 22px; height: 26px; }
  .accuracy {
    position: absolute; left: 418px; top: 556px;
    color: var(--white); font-weight: 900; font-size: 40px; line-height: 1;
    display: flex; align-items: baseline;
  }
  .accuracy .rate {
    font-family: "Roboto", sans-serif; font-weight: 700; font-size: 72px;
    color: var(--gold); margin-left: 10px;
  }
  .accuracy .pct { font-size: 46px; color: var(--gold); }
  .school {
    position: absolute; left: 0; top: 672px; width: 100%; height: 128px;
    background: var(--white);
    border-top: 3px solid var(--frame);
    display: flex; align-items: center; padding-left: 20px; gap: 30px;
  }
  .school__mark { width: 90px; height: 90px; border-radius: 50%; background: var(--ink); }
  .school__name { color: var(--ink); }
  .school__ja { font-weight: 700; font-size: 48px; line-height: 1.15; }
  .school__en { font-family: "Roboto", sans-serif; font-weight: 700; font-size: 28px; letter-spacing: 1px; }
</style>
</head>
<body>
  <div class="banner">
    <div class="banner__scene" role="img" aria-label="夕景のオフィス街に並ぶビジネスパーソンのシルエット写真"></div>

    <div class="ribbon">診断者数<span class="num">2</span>万人!</div>
    <div class="lead-band">キャリアアップのために何が必要か!</div>

    <p class="hook">「ビジネス能力」と「志向特性」をあぶりだす!?</p>
    <h1 class="title">スキル羅針盤</h1>
    <p class="tagline">~Age Of Discovery~</p>

    <a class="cta">詳しくはこちら
      <svg viewBox="0 0 22 26"><polygon points="0,0 22,13 0,26" fill="#ffffff"/></svg>
    </a>
    <p class="accuracy">診断結果整合率<span class="rate">84</span><span class="pct">%</span></p>

    <div class="school">
      <span class="school__mark"></span>
      <div class="school__name">
        <div class="school__ja">コスモリンク大学大学院</div>
        <div class="school__en">Cosmolink Graduate School of Business</div>
      </div>
    </div>
  </div>
</body>
</html>
```